We need a groovy retro poster for a comedy show called Shimmy Starfield :)

Hi there!
- We need a show poster for a comedy show called "Shimmy Starfield" starring Lydia Brenner.
- We want the show to have a retro groovy 60s/70s vibe with bright colors
- We will need some space to add dates and ticket info later.
- Please use 8.5 x 11 for sizing.

Target Market(s)

Men and women 40 and older, GenX

Industry/Entity Type

Entertainment

Requirements
Must have
• Artist Name: Lydia Brenner
Show Name: Shimmy Starfield
Show Description: A Night of Funky Laughs
Nice to have
• - We would like the headshot photo that is uploaded here to be more of a stylized in a cartoon/illustration way so that it is not just a photo.
- Colorful retro graphics.
- We have provided some samples that we like but are open to other ideas.
- We really like the Disco poster sample that is attached to the brief but would need the lady stylized with hair/face like Lydia
- We also like the style and colors of the Twirl Paradise poster attached to the brief but need the face/hair more like Lydia
- The postcard attached to the brief is just to give an example of branding colors that are currently being used. Not necessary to use them but just to give you an idea.
Should not have
• Please no trite references to stand up comedy such as stage and spotlight. A microphone is ok but only if it fits the illustration.

Thanks!

```html
<!DOCTYPE html>
<html lang="en">
<head>
<meta charset="utf-8">
<title>Shimmy Starfield — Lydia Brenner</title>
<link rel="stylesheet" href="https://fonts.googleapis.com/css2?family=Alfa+Slab+One&family=Pacifico&family=Roboto+Slab:wght@700&family=Roboto:wght@400&display=swap">
<style>
  :root {
    --coral: #de5b4a;
    --coral-dot: #f06650;
    --ink: #211712;
    --sun: #ffde5e;
    --red: #ff1a1a;
    --stripe-red: #c8323a;
    --stripe-orange: #ef553d;
  }
  * { margin: 0; padding: 0; box-sizing: border-box; }
  html, body { width: 927px; height: 1200px; overflow: hidden; }
  body { background: var(--coral); }

  .poster {
    position: relative;
    width: 927px;
    height: 1200px;
    background: var(--coral);
    overflow: hidden;
  }
  .frame {
    position: absolute;
    left: 75px; top: 41px;
    width: 777px; height: 1116px;
    border: 14px solid var(--ink);
  }
  .title-panel {
    position: absolute;
    left: 101px; top: 70px;
    width: 725px; height: 684px;
    background: var(--sun);
  }
  .stripe-art {
    position: absolute;
    left: 125px; top: 329px;
    width: 677px; height: 405px;
  }
  .portrait {
    position: absolute;
    left: 519px; top: 296px;
    width: 283px; height: 453px;
  }
  .show-name {
    position: absolute;
    left: 101px; top: 122px;
    width: 725px;
    text-align: center;
    font-family: "Alfa Slab One", serif;
    font-size: 146px;
    line-height: 1;
    color: var(--red);
    letter-spacing: -2px;
  }
  .show-name .line-top { display: block; }
  .show-name .line-script {
    display: block;
    margin-top: -92px;
    font-family: "Pacifico", cursive;
    font-size: 92px;
    line-height: 1.3;
    color: var(--ink);
    letter-spacing: 0;
  }
  .band {
    position: absolute;
    left: 125px;
    width: 677px;
    background: var(--ink);
    color: var(--sun);
    display: flex;
    align-items: center;
    justify-content: center;
  }
  .band-tagline {
    top: 780px; height: 95px;
    font-family: "Alfa Slab One", serif;
    font-size: 29px;
    letter-spacing: 0.5px;
  }
  .band-web {
    top: 1044px; height: 71px;
    font-family: "Roboto", sans-serif;
    font-size: 29px;
    letter-spacing: 0.5px;
  }
  .dot-rule {
    position: absolute;
    left: 145px;
    width: 620px; height: 10px;
    background-image: radial-gradient(circle, var(--coral-dot) 4.5px, transparent 5px);
    background-size: 21.5px 10px;
  }
  .dot-rule.upper { top: 893px; }
  .dot-rule.lower { top: 1028px; }
  .headliner {
    position: absolute;
    left: 101px; top: 896px;
    width: 725px;
    text-align: center;
    font-family: "Roboto Slab", serif;
    font-weight: 700;
    font-size: 47px;
    letter-spacing: 2px;
    line-height: 1;
    color: var(--ink);
  }
</style>
</head>
<body>
  <main class="poster">
    <div class="frame"></div>
    <section class="title-panel"></section>

    <svg class="stripe-art" viewBox="0 0 677 405" role="img" aria-label="Retro red and orange speed-line stripes fanning out behind the performer">
      <defs>
        <linearGradient id="stripeTone" x1="0" y1="0" x2="0" y2="1">
          <stop offset="0" stop-color="#ffde5e"/>
          <stop offset="0.45" stop-color="#e0703f"/>
          <stop offset="1" stop-color="#ef553d"/>
        </linearGradient>
      </defs>
      <rect width="677" height="405" fill="url(#stripeTone)"/>
    </svg>

    <svg class="portrait" viewBox="0 0 283 453" role="img" aria-label="Stylised black ink portrait of comedian Lydia Brenner with a bob haircut, smiling">
      <rect width="283" height="453" fill="#211712"/>
    </svg>

    <h1 class="show-name">
      <span class="line-top">SHIMMY</span>
      <span class="line-script">Starfield</span>
    </h1>

    <p class="band band-tagline">A NIGHT OF FUNKY LAUGHS</p>

    <div class="dot-rule upper"></div>
    <p class="headliner">WITH LYDIA BRENNER</p>
    <div class="dot-rule lower"></div>

    <p class="band band-web">WWW.LYDIABRENNER.COM</p>
  </main>
</body>
</html>
```